VerdantMed Business Card & Stationary
VerdantMed Pharmacy
VerdantMed Business Card & Stationary - Pharmacy/Pharmaceuticals
Creative Brief
Professional
Clara J Vandermeer RPh
Owner/Pharmacist
3870 FM 2209 Rd, Suite 200, Katy, TX 77495
281-555-0142 Can use any 10 numbers for illustration purposes
clara@verdantmed-example.com
www.verdantmed-example.com
We are looking for something very stylish and creative yet professional that will capture attention and reinforce our branding strategy efforts. We would also like to have the ability with whatever digital files are sent to us to be easily changed by printing company to so that we could interchange staff members names and titles on the business cards. Please use modern symbols for phone, mobile, fax, web. No QR code needed. Would like to see the drafts using the logo color variations (silver or gold or blue and gray/silver) in the logo upload files. Thank you.
Designers Creativity. Editable Fields - need to be able to modify and list the pharmacy's services that will be offered: Willow Health Clinic Quick and Convenient Drive Thru Compounding: Traditional, Specialty, Pet Immunizations and Health Screening Delivery
belvuto belvuto
Project is Unveiled. Looking forward to your work towards refining the cards. Thank you.

```html
<!DOCTYPE html>
<html lang="en">
<head>
<meta charset="utf-8">
<title>VerdantMed Pharmacy Stationery</title>
<link href="https://fonts.googleapis.com/css2?family=Lato:wght@300;400;700&display=swap" rel="stylesheet">
<style>
:root{
  --bg:#ebe2d4;
  --teal:#8fb4b3;
  --teal-dark:#5f8b8a;
  --teal-light:#d5e4e3;
  --gold:#b48a4c;
  --gold-light:#dcbb82;
  --paper:#ffffff;
  --ink:#5d6a6a;
  --line:#c9d6d5;
  --seal:#a3282b;
}
*{box-sizing:border-box;margin:0;padding:0}
html,body{width:1200px;height:235px;overflow:hidden}
body{background:var(--bg);font-family:'Lato',sans-serif;color:var(--ink);position:relative}
.piece{position:absolute;background:var(--paper);box-shadow:0 1px 3px rgba(0,0,0,.18);overflow:hidden}
.brand{display:flex;align-items:center;gap:3px;color:var(--teal-dark);font-weight:400;white-space:nowrap}
.brand .dot{width:.7em;height:.7em;border-radius:50%;background:var(--teal)}
.brand.light{color:#fff}
.brand.light .dot{background:#fff}
.band{position:absolute;left:0;right:0;background:var(--teal)}
.tiny{font-size:3.2px;line-height:1.45;white-space:nowrap}
.contact{display:flex;align-items:center;gap:2px;font-size:3.2px;line-height:1.5;white-space:nowrap}
.contact svg{width:3.4px;height:3.4px;fill:none;stroke:var(--teal-dark);stroke-width:2;flex:none}
.contact-row{display:flex;gap:6px;justify-content:center}
.services{list-style:none;font-size:3.2px;line-height:1.6}
.services li::before{content:"";display:inline-block;width:2px;height:2px;border-radius:50%;background:var(--teal-dark);margin-right:2px;vertical-align:middle}
.heading{font-size:4px;font-weight:700;color:var(--teal-dark);margin-bottom:2px}

/* business cards */
.card-front{left:10px;top:86px;width:130px;height:36px;background:linear-gradient(135deg,var(--gold-light),var(--gold));display:flex;align-items:center;justify-content:center}
.card-front .brand{font-size:9px}
.card-back{left:10px;top:126px;width:130px;height:36px;padding:4px 7px;display:flex;justify-content:space-between}
.card-back .name{font-size:4.6px;font-weight:700;color:var(--teal-dark)}
.card-back .role{font-size:3.4px;margin-bottom:2px}
.card-back .band{bottom:0;height:3px}

/* letterhead */
.letterhead{left:152px;top:16px;width:142px;height:204px;padding:12px 12px}
.letterhead .brand{font-size:8px;justify-content:center;margin-bottom:4px}
.letterhead .sub{text-align:center;font-size:3.2px;letter-spacing:.6px;margin-bottom:14px}
.letterhead p{font-size:3.4px;line-height:1.6;margin-bottom:5px;white-space:normal}
.letterhead .sig{font-weight:700;color:var(--teal-dark)}
.letterhead .band{bottom:14px;height:4px}
.letterhead .foot{position:absolute;bottom:3px;left:0;right:0}

/* disc */
.disc{left:318px;top:22px;width:90px;height:90px;border-radius:50%;background:radial-gradient(circle,var(--bg) 0 9px,#fff 10px 24px,var(--teal-light) 25px 45px)}
.disc .brand{position:absolute;left:0;right:0;top:62px;justify-content:center;font-size:6px}
.disc .tiny{position:absolute;left:0;right:0;top:71px;text-align:center}

/* window envelope */
.env-small{left:300px;top:168px;width:110px;height:44px}
.env-small .band{top:0;height:4px}
.env-small .brand{position:absolute;left:6px;top:8px;font-size:5px}
.env-small .ret{position:absolute;left:6px;top:15px}
.env-small .window{position:absolute;left:44px;top:24px;width:56px;height:12px;border:1px solid var(--line)}

/* seal */
.seal{position:absolute;left:528px;top:24px;width:34px;height:34px;border-radius:50%;background:radial-gradient(circle at 40% 35%,#c24346,var(--seal));box-shadow:0 1px 3px rgba(0,0,0,.3)}

/* note card */
.note{left:492px;top:88px;width:96px;height:62px;padding:7px 8px}
.note .brand{font-size:6.5px;margin-bottom:3px}
.note .band{bottom:0;height:5px}
.note-env{left:498px;top:158px;width:86px;height:24px;padding:5px 6px}
.note-env .brand{font-size:4.5px}
.note-env .band{bottom:0;height:3px}

/* tall envelope */
.env-tall{left:612px;top:38px;width:128px;height:192px}
.env-tall .flap{position:absolute;left:0;top:0;width:128px;height:62px}
.env-tall .brand{position:absolute;left:0;right:0;top:92px;justify-content:center;font-size:8px}
.env-tall .sub{position:absolute;left:0;right:0;top:104px;text-align:center}
.env-tall .band{bottom:0;height:6px}

/* folder */
.folder-cover{left:770px;top:30px;width:118px;height:196px;background:var(--teal)}
.folder-cover .brand{position:absolute;left:0;right:0;top:84px;justify-content:center;font-size:10px}
.folder-cover .sub{position:absolute;left:0;right:0;top:98px;text-align:center;color:#fff;font-size:3.6px;letter-spacing:.5px}
.folder-cover .foot{position:absolute;left:0;right:0;bottom:10px;text-align:center;color:#fff}
.folder-inner{left:890px;top:30px;width:118px;height:196px}
.folder-inner .pocket{position:absolute;left:0;bottom:0;width:118px;height:96px}
.folder-inner .info{position:absolute;left:10px;right:10px;top:12px}
.folder-inner .info .brand{font-size:6px;margin-bottom:6px}
.folder-inner .slot{position:absolute;right:14px;bottom:40px;width:32px;height:10px;border:1px solid #fff;border-radius:1px}

/* web screens */
.screen-wide{left:1022px;top:22px;width:110px;height:72px}
.nav{position:absolute;left:0;right:0;top:0;height:10px;background:var(--teal);display:flex;align-items:center;justify-content:space-between;padding:0 5px}
.nav .brand{font-size:5px}
.nav ul{list-style:none;display:flex;gap:4px;font-size:3px;color:#fff}
.hero{position:absolute;background:linear-gradient(90deg,var(--teal-light),var(--teal))}
.screen-wide .hero{left:6px;right:6px;top:14px;height:26px}
.hero-text{position:absolute;left:10px;top:22px;font-size:4.5px;color:var(--teal-dark);font-weight:700}
.cols{position:absolute;left:6px;right:6px;display:flex;gap:4px}
.cols div{flex:1;font-size:3px;line-height:1.4}
.cols b{display:block;color:var(--teal-dark);font-size:3.3px}
.screen-wide .cols{top:45px}
.screen-tablet{left:1124px;top:128px;width:68px;height:90px}
.screen-tablet .nav{height:8px}
.screen-tablet .nav .brand{font-size:4.2px}
.screen-tablet .hero{left:5px;right:5px;top:12px;height:22px}
.screen-tablet .body{position:absolute;left:6px;right:6px;top:38px}
</style>
</head>
<body>

<svg width="0" height="0" style="position:absolute">
  <defs>
    <symbol id="i-phone" viewBox="0 0 24 24"><path d="M5 3h4l2 5-3 2a12 12 0 0 0 6 6l2-3 5 2v4a2 2 0 0 1-2 2A18 18 0 0 1 3 5a2 2 0 0 1 2-2z"/></symbol>
    <symbol id="i-mobile" viewBox="0 0 24 24"><rect x="6" y="2" width="12" height="20" rx="2"/><path d="M11 18h2"/></symbol>
    <symbol id="i-fax" viewBox="0 0 24 24"><path d="M7 9V3h10v6"/><rect x="3" y="9" width="18" height="9" rx="1"/><path d="M7 15h10v6H7z"/></symbol>
    <symbol id="i-web" viewBox="0 0 24 24"><circle cx="12" cy="12" r="9"/><path d="M3 12h18M12 3c3 3 3 15 0 18M12 3c-3 3-3 15 0 18"/></symbol>
    <symbol id="i-mail" viewBox="0 0 24 24"><rect x="3" y="5" width="18" height="14" rx="1"/><path d="M3 6l9 7 9-7"/></symbol>
    <symbol id="i-pin" viewBox="0 0 24 24"><path d="M12 22s7-7 7-12a7 7 0 0 0-14 0c0 5 7 12 7 12z"/><circle cx="12" cy="10" r="2.5"/></symbol>
  </defs>
</svg>

<!-- business cards -->
<div class="piece card-front"><div class="brand light"><span class="dot"></span>VerdantMed</div></div>
<div class="piece card-back">
  <div>
    <div class="name">Clara J Vandermeer RPh</div>
    <div class="role">Owner/Pharmacist</div>
    <div class="contact"><svg><use href="#i-pin"/></svg>3870 FM 2209 Rd, Suite 200, Katy, TX 77495</div>
    <div class="contact"><svg><use href="#i-mail"/></svg>clara@verdantmed-example.com</div>
  </div>
  <div>
    <div class="contact"><svg><use href="#i-phone"/></svg>281-555-0142</div>
    <div class="contact"><svg><use href="#i-mobile"/></svg>281-555-0143</div>
    <div class="contact"><svg><use href="#i-fax"/></svg>281-555-0144</div>
    <div class="contact"><svg><use href="#i-web"/></svg>www.verdantmed-example.com</div>
  </div>
  <div class="band"></div>
</div>

<!-- letterhead -->
<div class="piece letterhead">
  <div class="brand"><span class="dot"></span>VerdantMed</div>
  <div class="sub">VerdantMed Pharmacy</div>
  <p>Dear Patient,</p>
  <p>Thank you for choosing us for your care. We look forward to serving you.</p>
  <div class="heading">Our Services</div>
  <ul class="services">
    <li>Willow Health Clinic</li>
    <li>Quick and Convenient Drive Thru</li>
    <li>Compounding: Traditional, Specialty, Pet</li>
    <li>Immunizations and Health Screening</li>
    <li>Delivery</li>
  </ul>
  <p style="margin-top:8px">Sincerely,</p>
  <p class="sig">Clara J Vandermeer RPh</p>
  <div class="band"></div>
  <div class="foot">
    <div class="contact-row">
      <div class="contact"><svg><use href="#i-pin"/></svg>3870 FM 2209 Rd, Suite 200, Katy, TX 77495</div>
    </div>
    <div class="contact-row">
      <div class="contact"><svg><use href="#i-phone"/></svg>281-555-0142</div>
      <div class="contact"><svg><use href="#i-web"/></svg>www.verdantmed-example.com</div>
    </div>
  </div>
</div>

<!-- disc -->
<div class="piece disc">
  <div class="brand"><span class="dot"></span>VerdantMed</div>
  <div class="tiny">VerdantMed Pharmacy</div>
</div>

<!-- window envelope -->
<div class="piece env-small">
  <div class="band"></div>
  <div class="brand"><span class="dot"></span>VerdantMed</div>
  <div class="ret">
    <div class="contact"><svg><use href="#i-pin"/></svg>3870 FM 2209 Rd, Suite 200, Katy, TX 77495</div>
  </div>
  <div class="window"></div>
</div>

<div class="seal" role="img" aria-label="Red wax seal"></div>

<!-- note card and envelope -->
<div class="piece note">
  <div class="brand"><span class="dot"></span>VerdantMed</div>
  <div class="tiny" style="margin-bottom:3px">Your health, our care</div>
  <ul class="services">
    <li>Quick and Convenient Drive Thru</li>
    <li>Immunizations and Health Screening</li>
    <li>Delivery</li>
  </ul>
  <div class="band"></div>
</div>
<div class="piece note-env">
  <div class="brand"><span class="dot"></span>VerdantMed</div>
  <div class="band"></div>
</div>

<!-- tall envelope -->
<div class="piece env-tall">
  <svg class="flap" viewBox="0 0 128 62" preserveAspectRatio="none"><path d="M0 0H128V40L64 62L0 40Z" fill="#8fb4b3"/></svg>
  <div class="brand"><span class="dot"></span>VerdantMed</div>
  <div class="sub">
    <div class="contact-row"><div class="contact"><svg><use href="#i-pin"/></svg>3870 FM 2209 Rd, Suite 200, Katy, TX 77495</div></div>
    <div class="contact-row"><div class="contact"><svg><use href="#i-web"/></svg>www.verdantmed-example.com</div></div>
  </div>
  <div class="band"></div>
</div>

<!-- folder -->
<div class="piece folder-cover">
  <div class="brand light"><span class="dot"></span>VerdantMed</div>
  <div class="sub">VerdantMed Pharmacy</div>
  <div class="foot tiny">www.verdantmed-example.com</div>
</div>
<div class="piece folder-inner">
  <div class="info">
    <div class="brand"><span class="dot"></span>VerdantMed</div>
    <div class="heading">Our Services</div>
    <ul class="services">
      <li>Willow Health Clinic</li>
      <li>Quick and Convenient Drive Thru</li>
      <li>Compounding: Traditional, Specialty, Pet</li>
      <li>Immunizations and Health Screening</li>
      <li>Delivery</li>
    </ul>
  </div>
  <svg class="pocket" viewBox="0 0 118 96" preserveAspectRatio="none"><path d="M0 30Q59 0 118 22V96H0Z" fill="#8fb4b3"/></svg>
  <div class="slot"></div>
</div>

<!-- website desktop -->
<div class="piece screen-wide">
  <div class="nav">
    <div class="brand light"><span class="dot"></span>VerdantMed</div>
    <ul><li>Home</li><li>About</li><li>Services</li><li>Contact</li></ul>
  </div>
  <div class="hero" role="img" aria-label="Website header photo of the pharmacy"></div>
  <div class="hero-text">Welcome to our pharmacy</div>
  <div class="cols">
    <div><b>Drive Thru</b>Quick and Convenient</div>
    <div><b>Compounding</b>Traditional, Specialty, Pet</div>
    <div><b>Delivery</b>Immunizations</div>
  </div>
</div>

<!-- website tablet -->
<div class="piece screen-tablet">
  <div class="nav"><div class="brand light"><span class="dot"></span>VerdantMed</div></div>
  <div class="hero" role="img" aria-label="Website header photo of the pharmacy"></div>
  <div class="body">
    <div class="heading">Our Services</div>
    <ul class="services">
      <li>Willow Health Clinic</li>
      <li>Drive Thru</li>
      <li>Compounding</li>
      <li>Delivery</li>
    </ul>
    <div class="contact" style="margin-top:3px"><svg><use href="#i-phone"/></svg>281-555-0142</div>
  </div>
</div>

</body>
</html>
```